Offshore Energy Projects Management Consultancy needs a business card design

Logo available. We provide teams to deliver engineering consultancy, project management and delivery teams mainly in the offshore renewables sector. The company is all about bringing the right people to a project to deliver the scope.

The business card will be used for all staff.

The business card should be quite simple, vibrant and uncluttered but convey experience, enthusiasm and integration.

Target Market(s)

Energy Project Developers and Tier 1 construction companies

Contact Information for Business Card

Logo should be on the back of the card. I'm happy for the designer to play with the colour of the logo and background colour.

Front of the card should convey all the must have information in a clear and professional manner but without being overly traditional.

Colors

Designer to choose colors to be used in the design.

Requirements
Must have
• Land Line Tel Number, Mobile Tel Number, Email, business address, web address.

```html
<!DOCTYPE html>
<html lang="en">
<head>
<meta charset="utf-8">
<title>Tidewell Partners – Business Card</title>
<link href="https://fonts.googleapis.com/css2?family=Arimo:wght@400;700&display=swap" rel="stylesheet">
<style>
  :root {
    --page-bg: #e6e8ea;
    --card-bg: #ffffff;
    --brand-deep: #1c74c4;
    --brand-bright: #29a8e3;
    --text-grey: #6d6e70;
    --rule-blue: #3d8fd6;
  }
  * { margin: 0; padding: 0; box-sizing: border-box; }
  html, body {
    width: 1200px; height: 1200px; overflow: hidden;
    background: var(--page-bg);
    font-family: "Arimo", Arial, sans-serif;
  }
  .stage {
    width: 1200px; height: 1200px;
    display: flex; flex-direction: column; align-items: center; justify-content: center;
    gap: 60px;
  }
  .card {
    position: relative;
    width: 860px; height: 490px;
    background: var(--card-bg);
    border-radius: 28px;
    box-shadow: 0 6px 18px rgba(0,0,0,0.12);
  }
  /* Back: logo side */
  .card--back { display: flex; align-items: center; justify-content: center; }
  .wordmark {
    display: flex; align-items: center; gap: 22px;
    font-weight: 700; color: var(--brand-deep);
  }
  .wordmark__dot {
    width: 26px; height: 26px; border-radius: 50%;
    background: var(--brand-bright);
  }
  .wordmark--large .wordmark__name { font-size: 68px; letter-spacing: 1px; }
  .wordmark--small { position: absolute; top: 58px; right: 70px; gap: 14px; }
  .wordmark--small .wordmark__name { font-size: 32px; }
  .wordmark--small .wordmark__dot { width: 16px; height: 16px; }

  /* Front: contact side */
  .main-rule {
    position: absolute; left: 90px; right: 70px; top: 212px;
    height: 2px; background: var(--rule-blue);
  }
  .person { position: absolute; left: 90px; top: 148px; }
  .person__name { font-size: 34px; color: var(--brand-deep); }
  .person__title { font-size: 19px; color: var(--text-grey); margin-top: 4px; }
  .short-rule {
    position: absolute; left: 90px; top: 262px; width: 200px;
    height: 2px; background: var(--rule-blue);
  }
  .contacts {
    position: absolute; left: 90px; top: 286px;
    list-style: none; color: var(--text-grey); font-size: 24px;
  }
  .contacts li { display: flex; align-items: center; gap: 18px; height: 40px; }
  .contacts svg { width: 18px; height: 18px; fill: var(--brand-deep); flex: none; }
  .address {
    position: absolute; right: 70px; top: 240px;
    display: flex; align-items: flex-end; gap: 14px;
    color: var(--text-grey); font-size: 24px; line-height: 1.3;
  }
  .address svg { width: 18px; height: 24px; fill: var(--brand-deep); margin-bottom: 4px; }
</style>
</head>
<body>
<main class="stage">
  <section class="card card--back">
    <div class="wordmark wordmark--large">
      <span class="wordmark__dot"></span>
      <span class="wordmark__name">Tidewell Partners</span>
    </div>
  </section>

  <section class="card card--front">
    <div class="wordmark wordmark--small">
      <span class="wordmark__dot"></span>
      <span class="wordmark__name">Tidewell Partners</span>
    </div>

    <div class="person">
      <p class="person__name">Morgan Hale</p>
      <p class="person__title">Chief Executive Officer</p>
    </div>
    <div class="main-rule"></div>
    <div class="short-rule"></div>

    <ul class="contacts">
      <li><svg viewBox="0 0 24 24"><path d="M6.6 10.8a15 15 0 0 0 6.6 6.6l2.2-2.2c.3-.3.7-.4 1-.2 1.1.4 2.3.6 3.6.6.6 0 1 .4 1 1V20c0 .6-.4 1-1 1A17 17 0 0 1 3 4c0-.6.4-1 1-1h3.5c.6 0 1 .4 1 1 0 1.3.2 2.5.6 3.6.1.3 0 .7-.2 1z"/></svg>xxx xxx xxxx</li>
      <li><svg viewBox="0 0 24 24"><path d="M2 9c5-5 15-5 20 0l-3 3-3-2V8c-2.6-.8-5.4-.8-8 0v2l-3 2zM5 14h14l1 6H4z"/></svg>xxx xxx xxxx</li>
      <li><svg viewBox="0 0 24 24"><path d="M2 5h20v14H2zm2 2v.5l8 5 8-5V7z"/></svg>info@xxxxxx.com</li>
      <li><svg viewBox="0 0 24 24"><path d="M12 2a10 10 0 1 0 0 20 10 10 0 0 0 0-20zm0 2c1 1.3 1.8 3 2 5h-4c.2-2 1-3.7 2-5zM4.2 11h3.9c.1 1.5.3 3 .8 4.2A8 8 0 0 1 4.2 11zm5.8 0h4c-.1 1.8-.8 3.6-2 5-1.2-1.4-1.9-3.2-2-5zm5.9 0h3.9a8 8 0 0 1-4.7 4.2c.5-1.2.7-2.7.8-4.2z"/></svg>www.xxxxxx.com</li>
    </ul>

    <div class="address">
      <svg viewBox="0 0 18 24"><path d="M9 0a9 9 0 0 0-9 9c0 6.5 9 15 9 15s9-8.5 9-15a9 9 0 0 0-9-9zm0 12.5A3.5 3.5 0 1 1 9 5.5a3.5 3.5 0 0 1 0 7z"/></svg>
      <p>418 Harbor Row, Suite 20<br>Portland, OR 97201</p>
    </div>
  </section>
</main>
</body>
</html>
```